School District In Need of Powerful Presentation

Create a modern PPT design template -- standard and widescreen -- for the Brisco RE-8K school district inspired by its logo. The presentation should be a modern projection of 21st education that excites the people who view it. The school district is located in a rural farming community with a view of the rocky mountains to its west (check out this picture www.tentstopatmarlowbend.com/AnimatedImages/HomeGallery/000MountainScene.jpg). People in this community want quality education for their children with opportunities for them to be successful after they graduate.

Target Market(s)

The Johnstown and Milliken communities in Northern Colorado

Industry/Entity Type

Education

Font styles to use
Sans Serif

Colors
ec1f27
3176b5
acd036
fece3e
f78f20

Requirements
Must have
• The name of the school district:
• Brisco County School District RE-8K Ardenvale-Toller
• Website address: www.briscore8k.k12.zq.us/
• Email: listen@briscore8k.org
Nice to have
• A couple of color options including their current color scheme: red, gold, black
• Placeholder for pictures of students and teachers
Should not have
• Please do not use the full logo in it's current for, but you may use elements of the logo.

```html
<!DOCTYPE html>
<html lang="en">
<head>
<meta charset="utf-8">
<title>Brisco RE-8K Presentation Template</title>
<link href="https://fonts.googleapis.com/css2?family=Lato:wght@300;400;700;900&family=Oswald:wght@600&display=swap" rel="stylesheet">
<style>
:root{
  --red:#b0161f;
  --red-dark:#8c0f16;
  --red-mid:#a52a2a;
  --red-soft:#c9575c;
  --gold:#e9c35c;
  --ink:#333;
  --muted:#9a9a9a;
  --paper:#fff;
  --stage:#000;
}
*{box-sizing:border-box;margin:0;padding:0}
html,body{width:886px;height:1200px;overflow:hidden;background:var(--stage)}
body{font-family:"Lato",sans-serif;color:var(--ink)}
.deck{display:grid;grid-template-columns:repeat(3,280px);grid-auto-rows:162px;gap:8px;padding:9px 11px;width:886px;height:1200px}
.slide{position:relative;background:var(--paper);overflow:hidden}
.slide-title{position:absolute;left:8px;top:7px;font-size:9px;color:var(--red);font-weight:400}
.slide-title.bold{font-weight:700;color:var(--red-dark);font-size:8px}
.slide-title .light{font-weight:300}
.badge{position:absolute;right:6px;top:6px;display:flex;align-items:center;gap:2px;font-size:5px;font-weight:700;color:var(--red)}
.badge i{display:block;width:9px;height:9px;border-radius:50%;border:1.2px solid var(--red)}
.footer{position:absolute;left:0;right:0;bottom:0;height:6px;background:var(--red);color:#fff;font-size:3.2px;line-height:6px;padding-left:4px}
.footer b{position:absolute;right:6px;bottom:0;width:10px;height:8px;background:#5a5a5a;font-size:3.2px;line-height:8px;text-align:center;font-weight:400}
.copy{font-size:3.4px;line-height:1.6;color:var(--muted);text-align:justify}
.photo{position:absolute}
.kicker{font-size:4.6px;font-weight:700;color:var(--red)}
.kicker.uline{border-bottom:.8px solid var(--red);display:inline-block;padding-bottom:1px}
.cover{background:radial-gradient(circle at 50% 40%,#b81d26,#7e0c12)}
.cover-title{position:absolute;top:52px;width:100%;text-align:center;font-family:"Oswald",sans-serif;font-size:15px;color:var(--gold);letter-spacing:.3px}
.cover-name{position:absolute;top:104px;width:100%;text-align:center;font-size:11px;font-weight:700;color:var(--gold);letter-spacing:.5px}
.cover-foot{position:absolute;bottom:0;left:0;right:0;height:7px;background:#555;color:#ddd;font-size:3.2px;line-height:7px;display:flex;justify-content:space-between;padding:0 5px}
.divider{background:linear-gradient(135deg,#b51c25,#8a0e15)}
.divider h2{position:absolute;top:72px;width:100%;text-align:center;color:#fff;font-size:10.5px;font-weight:900}
.divider p{position:absolute;top:90px;left:36px;right:36px;text-align:center;color:#f3d5d6;font-size:3.4px;line-height:1.6}
.divider .footer{background:#7a0b11}
.circle-img{position:absolute;border-radius:50%;background:var(--red);color:#fff;font-size:5.5px;font-weight:700;display:flex;align-items:center;justify-content:center;text-align:center;line-height:1.15}
.big-num{position:absolute;font-size:24px;font-weight:900;color:#ececec}
.num-block{position:absolute;left:0;width:89px;height:30px;color:rgba(255,255,255,.4);font-size:24px;font-weight:900;text-align:right;padding-right:2px;line-height:30px}
.table{position:absolute;left:8px;right:3px;top:34px;font-size:4px}
.table .row{display:grid;grid-template-columns:48px 1fr;align-items:center;height:18.5px;border-bottom:.6px solid #fff}
.table .row:nth-child(odd){background:#f0f0f0}
.table .row:nth-child(even){background:#fafafa}
.table .head{background:var(--red)!important;color:#fff;font-weight:700;height:13px}
.table .row span:first-child{padding-left:10px;color:var(--red);font-weight:700}
.table .head span:first-child{color:#fff}
.table .copy{font-size:3.2px;line-height:1.4;padding-right:4px}
.stat{position:absolute;text-align:center;width:40px}
.stat strong{display:block;font-size:9px;font-weight:700}
.stat em{display:block;font-style:normal;font-size:3.4px;color:#333;margin:1px 0}
.stat span{display:block;font-size:2.8px;color:var(--muted);line-height:1.4}
</style>
</head>
<body>
<main class="deck">

<section class="slide cover">
  <div class="cover-title">PROJECT TITLE HERE</div>
  <div class="cover-name">Brisco RE-8K</div>
  <div class="cover-foot"><span>Copyright text here</span><span>Author Name Here</span><span>http://www.briscore8k.k12.zq.us</span></div>
</section>

<section class="slide">
  <h3 class="slide-title"><span class="light">Welcome</span> Message !</h3>
  <div class="badge"><i></i>Brisco</div>
  <div class="photo" role="img" aria-label="Portrait photo of staff member" style="left:119px;top:40px;width:42px;height:42px;border-radius:50%;border:1px solid #ddd;background:linear-gradient(#e9e9e9,#b9bcc2)"></div>
  <div style="position:absolute;top:86px;width:100%;text-align:center"><div class="kicker" style="font-size:4px">EMPLOYEE NAME</div><div style="font-size:3px;color:#666">Company Name</div></div>
  <p class="copy" style="position:absolute;left:20px;right:20px;top:102px">Our students learn, build and grow with caring teachers in every classroom. Strong programs open bright paths for life after graduation day. Our students learn, build and grow with caring teachers in every classroom.</p>
  <p class="copy" style="position:absolute;left:20px;right:20px;top:134px">Strong programs open bright paths for life after graduation day. Our students learn and grow.</p>
  <div class="footer">Copyright text here<b>01</b></div>
</section>

<section class="slide">
  <h3 class="slide-title"><span class="light">CEO</span> Message !</h3>
  <div class="badge"><i></i>Brisco</div>
  <div class="photo" role="img" aria-label="Photo of smiling district leader" style="left:8px;top:30px;width:78px;height:126px;background:linear-gradient(160deg,#f3ece4,#cfd9e6)"></div>
  <div style="position:absolute;left:110px;top:44px;border-left:1.2px solid var(--red);padding-left:3px"><div style="font-size:6px;font-weight:700;color:var(--red-dark)">Employee Name</div></div>
  <div style="position:absolute;left:114px;top:53px;font-size:3px;color:#666">Designation</div>
  <p class="copy" style="position:absolute;left:114px;right:14px;top:61px">Our students learn, build and grow with caring teachers in every classroom. Strong programs open bright paths for life after graduation day. Our students learn, build and grow with caring teachers in every classroom. Strong programs open bright paths for life after graduation day.</p>
  <div style="position:absolute;left:70px;right:14px;top:108px;height:30px;background:#7b7b7b;color:#fff;font-size:3.6px;line-height:1.55;padding:4px 6px">“ Our students learn, build and grow with caring teachers in every classroom. Strong programs open bright paths for life after graduation. ”</div>
  <div class="footer">Copyright text here<b>01</b></div>
</section>

<section class="slide divider">
  <h2>SECTION DIVIDER HERE</h2>
  <p>Our students learn, build and grow with caring teachers in every classroom. Strong programs open bright paths for life after graduation day. Our students learn, build and grow.</p>
  <div class="footer">Copyright text here<b>01</b></div>
</section>

<section class="slide">
  <div class="photo" role="img" aria-label="Photo of hand with pen over charts and laptop" style="left:0;top:0;width:155px;height:156px;background:linear-gradient(135deg,#f4f4f4,#d6dbe3 60%,#9db4d6)"></div>
  <div class="badge"><i></i>Brisco</div>
  <div style="position:absolute;left:170px;top:35px;font-size:8px;color:var(--red-soft);font-weight:300">OUR PRODUCTS</div>
  <p class="copy" style="position:absolute;left:170px;right:14px;top:48px">Our students learn, build and grow with caring teachers in every classroom. Strong programs open bright paths for life after graduation day. Our students learn, build and grow with caring teachers in every classroom. Strong programs open bright paths for life after graduation day. Our students learn.</p>
  <div class="footer">Copyright text here<b>01</b></div>
</section>

<section class="slide">
  <div class="photo" role="img" aria-label="Photo of blue bar chart on screen" style="left:0;top:0;width:170px;height:156px;background:linear-gradient(150deg,#eef3fa,#8fb0dc 55%,#2f63ad)"></div>
  <div class="badge"><i></i>Brisco</div>
  <p class="copy" style="position:absolute;left:182px;right:10px;top:40px">Our students learn, build and grow with caring teachers in every classroom. Strong programs open bright paths for life after graduation day. Our students learn, build and grow with caring teachers in every classroom. Strong programs open bright paths for life after graduation day. Our students learn and grow.</p>
  <div class="footer">Copyright text here<b>01</b></div>
</section>

<section class="slide">
  <h3 class="slide-title"><span class="light">Main</span> Title Here</h3>
  <div class="badge"><i></i>Brisco</div>
  <div class="big-num" style="left:60px;top:34px">01</div>
  <div class="big-num" style="left:60px;top:74px">02</div>
  <div class="big-num" style="left:60px;top:114px">03</div>
  <div class="kicker uline" style="position:absolute;left:14px;top:34px">Section Title Here</div>
  <div class="kicker uline" style="position:absolute;left:14px;top:74px">Section Title Here</div>
  <div class="kicker uline" style="position:absolute;left:14px;top:114px">Section Title Here</div>
  <p class="copy" style="position:absolute;left:100px;right:8px;top:34px">Our students learn, build and grow with caring teachers in every classroom. Strong programs open bright paths for life after graduation day.</p>
  <p class="copy" style="position:absolute;left:100px;right:8px;top:74px">Our students learn, build and grow with caring teachers in every classroom. Strong programs open bright paths for life after graduation day.</p>
  <p class="copy" style="position:absolute;left:100px;right:8px;top:114px">Our students learn, build and grow with caring teachers in every classroom. Strong programs open bright paths for life after graduation day.</p>
  <div class="footer">Copyright text here<b>01</b></div>
</section>

<section class="slide">
  <h3 class="slide-title">Our Products</h3>
  <div class="badge"><i></i>Brisco</div>
  <div class="num-block" style="top:32px;background:var(--red)">01</div>
  <div class="num-block" style="top:72px;background:#b0393b">02</div>
  <div class="num-block" style="top:112px;background:var(--red)">03</div>
  <p class="copy" style="position:absolute;left:100px;right:8px;top:32px">Our students learn, build and grow with caring teachers in every classroom. Strong programs open bright paths for life after graduation day.</p>
  <p class="copy" style="position:absolute;left:100px;right:8px;top:72px">Our students learn, build and grow with caring teachers in every classroom. Strong programs open bright paths for life after graduation day.</p>
  <div class="footer">Copyright text here<b>01</b></div>
</section>

<section class="slide">
  <h3 class="slide-title">Our Services</h3>
  <div class="badge"><i></i>Brisco</div>
  <div class="kicker" style="position:absolute;left:14px;top:34px;font-size:4px">PRODUCT SUBTEXT HERE</div>
  <p class="copy" style="position:absolute;left:14px;right:82px;top:41px">Our students learn, build and grow with caring teachers in every classroom. Strong programs open bright paths for life after graduation day. Our students learn and grow.</p>
  <div class="kicker" style="position:absolute;left:14px;top:91px;font-size:4px">PRODUCT SUBTEXT HERE</div>
  <p class="copy" style="position:absolute;left:14px;right:82px;top:98px">Our students learn, build and grow with caring teachers in every classroom. Strong programs open bright paths for life after graduation day. Our students learn and grow.</p>
  <div class="circle-img" role="img" aria-label="Image placeholder" style="left:208px;top:30px;width:50px;height:50px">IMAGE<br>HERE</div>
  <div class="circle-img" role="img" aria-label="Image placeholder" style="left:208px;top:90px;width:50px;height:50px">IMAGE<br>HERE</div>
  <div class="footer">Copyright text here<b>01</b></div>
</section>

<section class="slide">
  <h3 class="slide-title"><span class="light">Logo Section here</span></h3>
  <div class="badge"><i></i>Brisco</div>
  <div style="position:absolute;left:18px;top:40px;width:26px;height:18px;border-radius:4px;background:#e4e4e4"></div>
  <div style="position:absolute;left:18px;top:80px;width:26px;height:18px;border-radius:4px;background:#e4e4e4"></div>
  <div style="position:absolute;left:18px;top:118px;width:26px;height:18px;border-radius:4px;background:#e4e4e4"></div>
  <p class="copy" style="position:absolute;left:62px;width:94px;top:36px">Our students learn, build and grow with caring teachers in every classroom.</p>
  <p class="copy" style="position:absolute;left:62px;width:94px;top:76px">Our students learn, build and grow with caring teachers in every classroom.</p>
  <p class="copy" style="position:absolute;left:62px;width:94px;top:115px">Our students learn, build and grow with caring teachers in every classroom.</p>
  <p class="copy" style="position:absolute;left:170px;right:10px;top:36px">Our students learn, build and grow with caring teachers in every classroom. Strong programs open bright paths for life after graduation day. Our students learn, build and grow with caring teachers in every classroom. Strong programs open bright paths for life after graduation day. Our students learn, build and grow with caring teachers in every classroom.</p>
  <div class="footer" style="background:transparent"><b style="background:var(--red)">01</b></div>
</section>

<section class="slide">
  <h3 class="slide-title">Bullet Slide</h3>
  <div class="badge"><i></i>Brisco</div>
  <div class="kicker" style="position:absolute;left:25px;top:33px">Bullet Title Here</div>
  <p class="copy" style="position:absolute;left:25px;right:12px;top:40px;font-size:3.8px">Our students learn, build and grow with caring teachers in every classroom. Strong programs open bright paths for life after graduation day. Our students learn, build and grow.</p>
  <div class="kicker" style="position:absolute;left:25px;top:73px">Bullet Title Here</div>
  <p class="copy" style="position:absolute;left:25px;right:12px;top:80px;font-size:3.8px">Our students learn, build and grow with caring teachers in every classroom. Strong programs open bright paths for life after graduation day. Our students learn, build and grow.</p>
  <div class="kicker" style="position:absolute;left:25px;top:113px">Bullet Title Here</div>
  <p class="copy" style="position:absolute;left:25px;right:12px;top:120px;font-size:3.8px">Our students learn, build and grow with caring teachers in every classroom. Strong programs open bright paths for life after graduation day. Our students learn, build and grow.</p>
  <div class="footer">Copyright text here<b>01</b></div>
</section>

<section class="slide">
  <h3 class="slide-title">Our Services</h3>
  <div class="badge"><i></i>Brisco</div>
  <div class="photo" role="img" aria-label="Photo of school building and lawn" style="left:0;top:22px;width:280px;height:73px;background:linear-gradient(#c9dbee 0%,#e9eef2 45%,#b09a8a 60%,#7f8e5a 100%)"></div>
  <div class="kicker" style="position:absolute;left:16px;top:106px;font-size:4px;font-weight:400">PRODUCT SUBTEXT HERE</div>
  <p class="copy" style="position:absolute;left:16px;width:100px;top:113px">Our students learn, build and grow with caring teachers in every classroom. Strong programs open bright paths for life after graduation.</p>
  <div class="kicker" style="position:absolute;left:140px;top:106px;font-size:4px;font-weight:400">PRODUCT SUBTEXT HERE</div>
  <p class="copy" style="position:absolute;left:140px;width:100px;top:113px">Our students learn, build and grow with caring teachers in every classroom. Strong programs open bright paths for life after graduation.</p>
  <div class="footer">Copyright text here<b>01</b></div>
</section>

<section class="slide">
  <h3 class="slide-title">Our Demo</h3>
  <div class="badge"><i></i>Brisco</div>
  <div class="photo" role="img" aria-label="Photo of printed charts on desk" style="left:0;top:28px;width:97px;height:134px;background:linear-gradient(135deg,#e8edf5,#6f95c7)"></div>
  <div style="position:absolute;left:97px;top:28px;width:107px;height:134px;background:var(--red-mid)"></div>
  <svg style="position:absolute;left:134px;top:44px" width="34" height="34" viewBox="0 0 34 34"><circle cx="17" cy="17" r="15" fill="none" stroke="#d87a7a" stroke-width="1"/><circle cx="17" cy="17" r="12" fill="none" stroke="#d87a7a" stroke-width=".6"/><text x="17" y="20" text-anchor="middle" font-family="Lato,sans-serif" font-size="8" fill="#fff">80%</text></svg>
  <p class="copy" style="position:absolute;left:108px;width:86px;top:86px;color:#f5d6d6">Our students learn, build and grow with caring teachers in every classroom.</p>
  <p class="copy" style="position:absolute;left:108px;width:86px;top:104px;color:#f5d6d6">Strong programs open bright paths for life after graduation day.</p>
  <p class="copy" style="position:absolute;left:108px;width:86px;top:122px;color:#f5d6d6">Strong programs open bright paths for life after graduation day.</p>
  <div class="photo" role="img" aria-label="Photo of hands typing on keyboard" style="left:204px;top:28px;width:76px;height:134px;background:linear-gradient(160deg,#fafafa,#c9c9cc)"></div>
  <div class="footer" style="background:transparent"><b style="background:var(--red)">01</b></div>
</section>

<section class="slide">
  <h3 class="slide-title">Our Demo</h3>
  <div class="badge"><i></i>Brisco</div>
  <p class="copy" style="position:absolute;left:14px;width:82px;top:42px">Our students learn, build and grow with caring teachers in every classroom.</p>
  <p class="copy" style="position:absolute;left:14px;width:82px;top:78px">Our students learn, build and grow with caring teachers in every classroom. Strong programs open bright paths for life after graduation day. Our students learn, build and grow.</p>
  <svg style="position:absolute;left:106px;top:33px" width="56" height="117" viewBox="0 0 56 117">
    <rect x="0" y="0" width="56" height="117" rx="4" fill="#222"/>
    <rect x="4" y="12" width="48" height="90" fill="#fff"/>
    <rect x="4" y="12" width="48" height="46" fill="#3c8ee0"/>
    <rect x="4" y="58" width="24" height="22" fill="#8bc34a"/>
    <rect x="28" y="58" width="24" height="22" fill="#f0782d"/>
    <rect x="4" y="80" width="24" height="22" fill="#f6c026"/>
    <rect x="28" y="80" width="24" height="22" fill="#e34234"/>
    <path d="M22 35l4 4 8-9" fill="none" stroke="#fff" stroke-width="2" stroke-linecap="round" stroke-linejoin="round"/>
    <circle cx="28" cy="109" r="3" fill="none" stroke="#555" stroke-width=".8"/>
  </svg>
  <p class="copy" style="position:absolute;left:174px;width:88px;top:42px">Our students learn, build and grow with caring teachers in every classroom.</p>
  <p class="copy" style="position:absolute;left:174px;width:88px;top:78px">Our students learn, build and grow with caring teachers in every classroom.</p>
  <p class="copy" style="position:absolute;left:174px;width:88px;top:112px">Our students learn, build and grow with caring teachers in every classroom.</p>
  <div class="footer">Copyright text here<b>01</b></div>
</section>

<section class="slide">
  <h3 class="slide-title">Our Demo</h3>
  <div class="badge"><i></i>Brisco</div>
  <div class="table">
    <div class="row head"><span>SECTION</span><span>MAIN TITLE HERE</span></div>
    <div class="row"><span>ICON - 1</span><span class="copy">Our students learn, build and grow with caring teachers in every classroom. Strong programs open bright paths.</span></div>
    <div class="row"><span>ICON - 1</span><span class="copy">Our students learn, build and grow with caring teachers in every classroom. Strong programs open bright paths.</span></div>
    <div class="row"><span>ICON - 1</span><span class="copy">Our students learn, build and grow with caring teachers in every classroom. Strong programs open bright paths.</span></div>
    <div class="row"><span>ICON - 1</span><span class="copy">Our students learn, build and grow with caring teachers in every classroom. Strong programs open bright paths.</span></div>
    <div class="row"><span>ICON - 1</span><span class="copy">Our students learn, build and grow with caring teachers in every classroom. Strong programs open bright paths.</span></div>
  </div>
  <div class="footer">Copyright text here<b>01</b></div>
</section>

<section class="slide">
  <h3 class="slide-title bold" style="color:#1f3a5a">Our Demo</h3>
  <div class="badge"><i></i>Brisco</div>
  <svg style="position:absolute;left:0;top:0" width="280" height="162" viewBox="0 0 280 162">
    <path d="M0 135 C20 140 40 120 54 94 S90 110 102 110 S135 95 150 96 S185 95 198 86 S225 55 240 45" fill="none" stroke="#666" stroke-width=".6" stroke-dasharray="1.5 1.5"/>
    <circle cx="54" cy="94" r="9" fill="var(--red)"/><circle cx="54" cy="94" r="3" fill="none" stroke="#fff" stroke-width="1"/>
    <circle cx="102" cy="110" r="9" fill="var(--red)"/><path d="M99 106h6v4l-3 3-3-3z" fill="#fff"/>
    <circle cx="150" cy="96" r="9" fill="var(--red)"/><text x="150" y="100" text-anchor="middle" font-size="10" font-weight="900" fill="#fff" font-family="Lato,sans-serif">”</text>
    <circle cx="198" cy="86" r="9" fill="var(--red)"/><path d="M194 90l8-8-2 7z" fill="#fff"/>
    <path d="M240 45l22-10-10 18-3-6z" fill="#ddd"/>
  </svg>
  <div class="stat" style="left:34px;top:34px"><strong>12%</strong><em>Concept &amp; Ideas</em><span>Our students learn and grow with caring teachers.</span></div>
  <div class="stat" style="left:82px;top:46px"><strong>37%</strong><em>Flash Sale</em><span>Our students learn and grow with caring teachers.</span></div>
  <div class="stat" style="left:130px;top:116px"><strong>25%</strong><em>Business Style</em><span>Our students learn and grow with caring teachers.</span></div>
  <div class="stat" style="left:182px;top:26px"><strong>9%</strong><em>Get Awards</em><span>Our students learn and grow with caring teachers.</span></div>
  <div class="stat" style="left:236px;top:62px"><em>Company Goal</em><span>Our students learn and grow with caring teachers.</span></div>
  <div class="footer" style="background:transparent"><b style="background:#444">01</b></div>
</section>

<section class="slide">
  <h3 class="slide-title bold">Graph Slide</h3>
  <div class="badge"><i></i>Brisco</div>
  <svg style="position:absolute;left:0;top:0" width="280" height="162" viewBox="0 0 280 162">
    <path d="M24 115 Q40 112 46 95 Q52 112 70 115z" fill="#c97a7a"/>
    <path d="M50 115 Q66 110 76 72 Q86 110 104 115z" fill="#a43a3a"/>
    <path d="M84 115 Q104 110 114 42 Q124 110 146 115z" fill="var(--red)"/>
    <path d="M126 115 Q140 110 146 80 Q152 110 168 115z" fill="#bd5a5a"/>
    <path d="M150 115 Q168 110 178 60 Q188 110 206 115z" fill="#a43a3a"/>
    <path d="M188 115 Q200 112 206 95 Q212 112 226 115z" fill="#c97a7a"/>
    <path d="M210 115 Q222 112 228 100 Q234 112 250 115z" fill="var(--red)"/>
    <line x1="14" y1="115" x2="266" y2="115" stroke="#ccc" stroke-width=".5"/>
    <g fill="var(--red)"><circle cx="44" cy="80" r="4.5"/><circle cx="76" cy="58" r="4.5"/><circle cx="114" cy="28" r="4.5"/><circle cx="146" cy="66" r="4.5"/><circle cx="178" cy="46" r="4.5"/><circle cx="206" cy="80" r="4.5"/><circle cx="228" cy="85" r="4.5"/></g>
  </svg>
  <p class="copy" style="position:absolute;left:14px;width:110px;top:124px;color:#c97a7a">Our students learn, build and grow with caring teachers in every classroom day.</p>
  <p class="copy" style="position:absolute;left:150px;width:110px;top:124px;color:#c97a7a">Our students learn, build and grow with caring teachers in every classroom day.</p>
  <div class="footer" style="background:transparent"><b style="background:#444">01</b></div>
</section>

<section class="slide">
  <h3 class="slide-title bold">Graph 2</h3>
  <div class="badge"><i></i>Brisco</div>
  <svg style="position:absolute;left:0;top:0" width="280" height="162" viewBox="0 0 280 162">
    <g stroke="#bbb" stroke-width=".4"><line x1="20" y1="48" x2="20" y2="115"/><line x1="86" y1="48" x2="86" y2="115"/><line x1="150" y1="48" x2="150" y2="115"/><line x1="216" y1="48" x2="216" y2="115"/><line x1="20" y1="115" x2="270" y2="115"/></g>
    <rect x="30" y="104" width="9" height="11" fill="#d9b0b0"/><rect x="39" y="96" width="9" height="19" fill="#a43a3a"/><rect x="48" y="86" width="9" height="29" fill="#8c1d1d"/><rect x="57" y="74" width="9" height="41" fill="var(--red)"/>
    <rect x="96" y="106" width="9" height="9" fill="#d9b0b0"/><rect x="105" y="98" width="9" height="17" fill="#a43a3a"/><rect x="114" y="100" width="9" height="15" fill="#8c1d1d"/><rect x="123" y="92" width="9" height="23" fill="var(--red)"/>
    <rect x="160" y="48" width="9" height="67" fill="var(--red)"/><rect x="169" y="74" width="9" height="41" fill="#8c1d1d"/><rect x="178" y="66" width="9" height="49" fill="#a43a3a"/><rect x="187" y="84" width="9" height="31" fill="#d9b0b0"/>
    <rect x="226" y="90" width="9" height="25" fill="#d9b0b0"/><rect x="235" y="76" width="9" height="39" fill="#a43a3a"/><rect x="244" y="60" width="9" height="55" fill="#8c1d1d"/><rect x="253" y="106" width="9" height="9" fill="var(--red)"/>
  </svg>
  <p class="copy" style="position:absolute;left:20px;width:110px;top:124px">Our students learn, build and grow with caring teachers in every classroom. Strong programs open paths.</p>
  <p class="copy" style="position:absolute;left:150px;width:110px;top:124px">Our students learn, build and grow with caring teachers in every classroom. Strong programs open paths.</p>
  <div class="footer" style="background:transparent"><b style="background:#444">01</b></div>
</section>

<section class="slide">
  <h3 class="slide-title bold" style="border-left:1.2px solid var(--red);padding-left:3px">Contact Us</h3>
  <div class="photo" role="img" aria-label="World map with office locations" style="left:16px;top:28px;width:248px;height:120px;background:radial-gradient(ellipse at 50% 50%,#d4d4d4,#ececec 70%,#fff)"></div>
  <svg style="position:absolute;left:0;top:0" width="280" height="162" viewBox="0 0 280 162">
    <path d="M60 70 Q110 50 160 75 Q200 60 220 80" fill="none" stroke="#555" stroke-width=".5"/>
    <path d="M70 95 Q130 110 165 95 Q210 110 230 130" fill="none" stroke="#555" stroke-width=".5"/>
    <g fill="#333"><path d="M68 40h7v6l-3.5 3-3.5-3z"/><path d="M192 50h7v6l-3.5 3-3.5-3z"/><path d="M103 77h7v6l-3.5 3-3.5-3z"/><path d="M165 72h7v6l-3.5 3-3.5-3z"/></g>
    <g fill="#333"><circle cx="60" cy="70" r="1.5"/><circle cx="160" cy="75" r="1.5"/><circle cx="220" cy="80" r="1.5"/><circle cx="70" cy="95" r="1.5"/><circle cx="165" cy="95" r="1.5"/><circle cx="230" cy="130" r="1.5"/></g>
  </svg>
  <div class="footer" style="background:transparent"><b style="background:var(--red)">01</b></div>
</section>

<section class="slide" style="background:var(--red)">
  <h2 style="position:absolute;top:58px;width:100%;text-align:center;color:#fff;font-size:10px;font-weight:700">Contact Addess</h2>
  <p style="position:absolute;left:22px;width:114px;top:78px;text-align:center;color:#f6dcdc;font-size:4.4px;line-height:1.6">Our students learn, build and grow with caring teachers in every classroom. Strong programs open bright paths for life after graduation.</p>
  <p style="position:absolute;left:144px;width:114px;top:78px;color:#f6dcdc;font-size:4.4px;line-height:1.6">Our students learn, build and grow with caring teachers in every classroom. Strong programs open bright paths for life after graduation.</p>
  <div class="footer" style="background:transparent"><b style="background:#444">01</b></div>
</section>

<section class="slide">
  <div class="photo" role="img" aria-label="Faint city skyline photo in red tone" style="left:0;top:0;width:280px;height:110px;background:linear-gradient(#b9262d,#9a1219)"></div>
  <h2 style="position:absolute;top:54px;width:100%;text-align:center;color:#fff;font-size:10px;font-weight:900">THANKS YOUR VERY MUCH</h2>
  <div style="position:absolute;left:20px;top:131px;font-size:5.5px;color:var(--muted)">Contact Details Here</div>
  <p class="copy" style="position:absolute;left:110px;width:110px;top:122px">Our students learn, build and grow with caring teachers in every classroom. Strong programs open bright paths for life.</p>
  <div class="footer" style="background:transparent"><b style="background:#444">01</b></div>
</section>

</main>
</body>
</html>
```